Zalvan Advertising & Publicity business cards

I would like my Company's business card to be designed creatively & profissionally the logo is attached in both Arabic & english and prefer to have my emblem dimmed on the card as well
-Logo ( Arabic & English)
-Name (Arabic & English)
-Title ( Arabic & English)
-----------
-Location
-Landline (icon)
-Mobile phone (icon)
-Email (icon)
-Instagram (icon)
-WhatsApp (icon)

Target Market(s)

Industry/Entity Type

Marketing

Contact Information for Business Card

-Logo ( Arabic & English)
-Name (Arabic & English)
-----------
-Location
-Landline (icon)
-Mobile phone (icon)
-Email (icon)
-Instagram (icon)
-WhatsApp (icon)

Font styles to use
Serif

Requirements
Must have
• all what is mentions in business card details blanked and i will add the data my self
Nice to have
• Dim emblem on my business card both Arabic & english

```html
<!DOCTYPE html>
<html lang="en">
<head>
<meta charset="utf-8">
<title>Zalvan Advertising & Publicity – Business Cards</title>
<link rel="stylesheet" href="https://fonts.googleapis.com/css2?family=Questrial&family=Noto+Kufi+Arabic:wght@400;700&family=Amiri&display=swap">
<style>
  :root {
    --page: #ffffff;
    --card: #ffffff;
    --ink: #111111;
    --ink-soft: #555555;
    --teal: #3cc1bd;
    --teal-faint: #b7e4e2;
    --shadow: rgba(0,0,0,0.22);
  }
  * { margin: 0; padding: 0; box-sizing: border-box; }
  html, body { width: 1001px; height: 1200px; overflow: hidden; background: var(--page); }
  .canvas { position: relative; width: 1001px; height: 1200px; }

  .card {
    position: absolute; left: 50px; width: 902px; height: 502px;
    background: var(--card); overflow: hidden;
    box-shadow: 0 2px 8px var(--shadow);
  }
  .card--front { top: 78px; }
  .card--back { top: 622px; }

  .emblem-faint {
    position: absolute;
    background: linear-gradient(135deg, var(--teal-faint), #d3efee);
  }
  .card--front .emblem-faint--large { left: 0; top: 0; width: 238px; height: 486px; clip-path: polygon(0 0, 30% 18%, 100% 50%, 30% 82%, 0 100%); }
  .card--front .emblem-faint--small { left: 833px; top: 210px; width: 69px; height: 78px; clip-path: polygon(100% 0, 0 50%, 100% 100%); }
  .card--back .emblem-faint--large { left: 670px; top: 14px; width: 232px; height: 480px; clip-path: polygon(100% 0, 70% 18%, 0 50%, 70% 82%, 100% 100%); }
  .card--back .emblem-faint--small { left: 0; top: 206px; width: 67px; height: 84px; clip-path: polygon(0 0, 100% 50%, 0 100%); }

  .brand-mark {
    position: absolute; width: 96px; height: 96px;
    background: var(--teal); transform: translate(-50%, -50%) rotate(45deg);
  }
  .card--front .brand-mark { left: 337px; top: 247px; }
  .card--back .brand-mark { left: 559px; top: 251px; }

  .divider { position: absolute; width: 2px; background: var(--ink); }
  .card--front .divider { left: 428px; top: 180px; height: 144px; }
  .card--back .divider { left: 472px; top: 176px; height: 140px; }

  .latin { font-family: "Questrial", "Century Gothic", sans-serif; }
  .arabic { font-family: "Noto Kufi Arabic", sans-serif; direction: rtl; }

  .brand-name--en { position: absolute; left: 444px; top: 160px; font-size: 108px; font-weight: 400; line-height: 1; color: var(--ink); }
  .tagline--en { position: absolute; left: 448px; top: 290px; font-size: 26px; color: var(--ink); }

  .contact { position: absolute; list-style: none; font-size: 22px; line-height: 25px; }
  .contact--en { left: 448px; top: 344px; color: var(--ink); }
  .contact--en li { display: flex; }
  .contact--en .label { width: 112px; }
  .contact--en .value { color: var(--ink-soft); }

  .brand-name--ar { position: absolute; right: 450px; top: 150px; font-size: 90px; font-weight: 700; line-height: 1.1; color: var(--ink); }
  .tagline--ar { position: absolute; right: 450px; top: 284px; font-size: 22px; font-weight: 700; color: var(--ink); }

  .contact--ar { right: 432px; top: 340px; font-size: 21px; }
  .contact--ar li { display: flex; flex-direction: row; gap: 14px; }
  .contact--ar .label { width: 82px; color: var(--ink); }
  .contact--ar .value {
    direction: ltr; unicode-bidi: bidi-override; color: var(--ink-soft);
    font-family: "Amiri", "Times New Roman", serif; font-size: 22px;
  }
</style>
</head>
<body>
<main class="canvas">

  <section class="card card--front" aria-label="Business card, English side">
    <div class="emblem-faint emblem-faint--large" role="img" aria-label="Faint brand emblem decoration"></div>
    <div class="emblem-faint emblem-faint--small" role="img" aria-label="Faint brand emblem decoration"></div>
    <div class="brand-mark" aria-hidden="true"></div>
    <div class="divider"></div>
    <h1 class="brand-name--en latin">Zalvan</h1>
    <p class="tagline--en latin">Advertising and Publicity</p>
    <ul class="contact contact--en latin">
      <li><span class="label">Landline</span><span class="value">: + 961 1 234 567</span></li>
      <li><span class="label">Mobile</span><span class="value">: + 961 3 111 222</span></li>
      <li><span class="label">Whatsapp</span><span class="value">: + 961 3 111 222</span></li>
      <li><span class="label">Email</span><span class="value">: www.zalvanads.com</span></li>
      <li><span class="label">Instagram</span><span class="value">: zalvanads</span></li>
    </ul>
  </section>

  <section class="card card--back" aria-label="Business card, Arabic side">
    <div class="emblem-faint emblem-faint--large" role="img" aria-label="Faint brand emblem decoration"></div>
    <div class="emblem-faint emblem-faint--small" role="img" aria-label="Faint brand emblem decoration"></div>
    <div class="brand-mark" aria-hidden="true"></div>
    <div class="divider"></div>
    <h2 class="brand-name--ar arabic">زالفان</h2>
    <p class="tagline--ar arabic">للدعاية والإعلان</p>
    <ul class="contact contact--ar arabic">
      <li><span class="label">هاتف</span><span class="value">٥٦٧ ٢٣٤ ١ ٩٦١ + :</span></li>
      <li><span class="label">موبايل</span><span class="value">٢٢٢ ١١١ ٣ ٩٦١ + :</span></li>
      <li><span class="label">واتساب</span><span class="value">٢٢٢ ١١١ ٣ ٩٦١ + :</span></li>
      <li><span class="label">ايميل</span><span class="value">www.zalvanads.com :</span></li>
      <li><span class="label">انستغرام</span><span class="value">zalvanads :</span></li>
    </ul>
  </section>

</main>
</body>
</html>
```